Postcard design for accounting company

We need a postcard design (front and back) to our accounting firm that provides bookkeeping services to small and mid-size companies using TallyHive Online. We would like to see designs that use the color blue and match our overall branding (see website). The final design should communicate professionalism, trust, and ease.

Target Market(s)

Small and Mid-Size companies

Industry/Entity Type

Accounting

Colors
0054AA
0677BA
7BADD7
CADEEF
E8F1F8

Requirements
Must have
• Logo, contact information, indicate services offered, color blue, and fit postcard template (see attached). Contact info = 555.203.8841, 1.800.555.0142, Info@FernwayAccounting.example, www.FernwayAccounting.example. Use the PLMX Retail Indicia, which is a postage payment mark that takes the place of a regular postage stamp or meter stamp. Every PLMX mailpiece must include the PLMX Retail Indicia above and to the right of the address block. The PLMX Retail Indicia does not have a specific size requirement but must be larger than 0.5" x 0.5". The type font must be in all caps and at least a 4 point size. It should fit in the area 1.625" from the right edge and 1.375" from top edge. Leave 1/8" of space around the top and right edge. See attached sample.
Nice to have
• Include that we a re Certified TallyHive CertiGuides (can include THO logo). Also, maybe include the logos of the associations we are members of (Pine Hollow Chamber of Commerce, Continental Guild of Certified Ledgerkeepers, and Federated League of Female Enterprise Founders.

```html
<!DOCTYPE html>
<html lang="en">
<head>
<meta charset="utf-8">
<title>Fernway Accounting Postcard</title>
<link href="https://fonts.googleapis.com/css2?family=Montserrat:wght@400;500;600;700;800&display=swap" rel="stylesheet">
<style>
:root{
  --navy:#1c2f66;
  --blue:#0054AA;
  --mid:#0677BA;
  --sky:#7BADD7;
  --pale:#CADEEF;
  --mist:#E8F1F8;
  --teal:#2bb3c8;
  --ink:#1b1f2a;
  --stage:#e3e4e6;
  --white:#ffffff;
}
*{margin:0;padding:0;box-sizing:border-box}
html,body{width:1200px;height:2293px;overflow:hidden}
body{background:var(--stage);font-family:'Montserrat',sans-serif;position:relative;color:var(--ink)}
.card{position:absolute;left:42px;width:930px;height:620px;background:var(--white);overflow:hidden;box-shadow:0 4px 14px rgba(0,0,0,.18);transform:scale(1.2);transform-origin:0 0}
.card--front{top:372px}
.card--back{top:1176px}
.shapes{position:absolute;inset:0;width:100%;height:100%}
.abs{position:absolute}
.brand{left:32px;top:58px;display:flex;align-items:center;gap:12px}
.brand__mark{width:34px;height:34px;background:var(--blue)}
.brand__name{font-weight:700;font-size:27px;color:var(--blue);letter-spacing:-.3px}
.headline{left:32px;top:160px}
.headline__main{font-weight:800;font-size:40px;color:var(--mid);letter-spacing:1px;line-height:44px}
.headline__sub{font-weight:800;font-size:27px;color:var(--navy);line-height:32px;letter-spacing:.5px}
.rule{height:2px;background:var(--mid)}
.lede{left:32px;top:262px;font-size:15.5px;line-height:18.5px;color:var(--ink)}
.certified{left:32px;top:356px;font-weight:600;font-size:16.5px;line-height:19px;color:var(--ink)}
.seal{width:92px;height:92px;border-radius:50%;border:2px solid var(--navy);background:var(--white);display:flex;align-items:center;justify-content:center}
.seal__core{width:78px;height:78px;border-radius:50%;background:var(--mid)}
.pill{background:var(--teal);color:var(--white);border-radius:20px;font-weight:600;font-size:22px;letter-spacing:.8px;height:40px;display:flex;align-items:center;padding:0 16px}
.contact{left:32px;display:flex;flex-direction:column;gap:9px}
.contact__row{display:flex;align-items:center;gap:12px;font-size:16px;font-weight:500;letter-spacing:.3px;color:var(--ink);height:30px;white-space:nowrap}
.contact__row--bold{font-weight:700}
.contact__icon{width:30px;height:30px;border-radius:50%;background:var(--navy);display:flex;align-items:center;justify-content:center;flex:none}
.photo{position:absolute;inset:0}
.services-title{left:32px;top:32px}
.service{position:absolute;top:92px;display:flex;flex-direction:column;align-items:flex-start;gap:10px;color:var(--white);font-weight:600;font-size:12.5px;letter-spacing:.3px;white-space:nowrap}
.service__icon{width:54px;height:54px;border-radius:50%;background:var(--white);border:3px solid var(--sky);display:flex;align-items:center;justify-content:center}
.packages-title{left:32px;top:205px;color:var(--white);font-size:19px;font-weight:500;letter-spacing:.8px}
.pkg{position:absolute;top:236px;list-style:none;color:var(--white);font-size:13px;letter-spacing:.5px;line-height:15.5px;white-space:nowrap}
.pkg li{position:relative;padding-left:12px;margin-bottom:1.5px}
.pkg li::before{content:"";position:absolute;left:0;top:5px;width:5px;height:5px;border-radius:50%;background:var(--teal)}
.badges{left:32px;top:325px;display:flex;align-items:center;gap:22px}
.badge{width:76px;height:76px;border-radius:50%;background:var(--pale);border:3px solid var(--sky)}
.badge--shield{border-radius:6px 6px 38px 38px;width:58px;background:var(--mist);border-color:var(--mid)}
.badge--ring{background:var(--white);border:6px solid var(--mid)}
.badge-divider{width:1px;height:60px;background:#c9ced6}
.indicia{left:743px;top:32px;width:155px;height:155px;border:1.5px solid var(--ink);display:flex;align-items:center;justify-content:center;text-align:center;font-size:16px;font-weight:500;line-height:21.5px;letter-spacing:.4px}
.address-line{position:absolute;height:1.5px;background:var(--ink);right:32px}
</style>
</head>
<body>

<section class="card card--front" aria-label="Postcard front">
  <svg class="shapes" viewBox="0 0 930 620" preserveAspectRatio="none" aria-hidden="true">
    <defs>
      <linearGradient id="stripeA" x1="0" y1="0" x2="0" y2="1">
        <stop offset="0" stop-color="#22a9c2"/><stop offset="1" stop-color="#1c2f66"/>
      </linearGradient>
      <linearGradient id="photoTone" x1="0" y1="0" x2="1" y2="1">
        <stop offset="0" stop-color="#f4e7d8"/><stop offset=".45" stop-color="#c9d3de"/><stop offset="1" stop-color="#56657e"/>
      </linearGradient>
    </defs>
    <polygon points="0,440 450,440 510,620 0,620" fill="#E8F1F8"/>
    <polygon points="345,0 930,0 930,620 527,620" fill="url(#photoTone)"/>
    <polygon points="335,0 350,0 330,25" fill="#3f6d9a"/>
    <polygon points="840,0 930,0 930,200" fill="url(#stripeA)" opacity=".9"/>
    <polygon points="395,330 425,330 515,620 485,620" fill="url(#stripeA)"/>
    <polygon points="395,466 420,466 470,620 445,620" fill="url(#stripeA)"/>
  </svg>
  <div class="photo" role="img" aria-label="Photo of a business team reviewing documents at a glass table" style="clip-path:polygon(345px 0,930px 0,930px 620px,527px 620px)"></div>

  <div class="abs brand"><span class="brand__mark"></span><span class="brand__name">Fernway Accounting</span></div>

  <div class="abs headline">
    <div class="headline__main">ACCOUNTING</div>
    <div class="headline__sub">FOR YOUR BUSINESS</div>
  </div>
  <div class="abs rule" style="left:32px;top:247px;width:255px"></div>
  <p class="abs lede">Specializing in Cloud-Based<br>Bookkeeping and Payroll Processing<br>with TallyHive Online by Hivecraft.</p>

  <div class="abs rule" style="left:32px;top:344px;width:250px;height:1.5px"></div>
  <p class="abs certified">We are Certified<br>TallyHive CertiGuides</p>
  <div class="abs rule" style="left:32px;top:403px;width:250px;height:1.5px"></div>
  <div class="abs seal" style="left:265px;top:329px" role="img" aria-label="Certification seal"><span class="seal__core"></span></div>

  <div class="abs pill" style="left:32px;top:420px">Contact Us</div>
  <div class="abs contact" style="top:477px">
    <div class="contact__row contact__row--bold"><span class="contact__icon"><svg width="14" height="14" viewBox="0 0 24 24"><path d="M6.6 10.8a15 15 0 0 0 6.6 6.6l2.2-2.2a1 1 0 0 1 1-.25 11.4 11.4 0 0 0 3.6.6 1 1 0 0 1 1 1V20a1 1 0 0 1-1 1A17 17 0 0 1 3 4a1 1 0 0 1 1-1h3.5a1 1 0 0 1 1 1c0 1.25.2 2.45.6 3.6a1 1 0 0 1-.25 1z" fill="#fff"/></svg></span>555.203.8841 / 1.800.555.0142</div>
    <div class="contact__row"><span class="contact__icon"><svg width="14" height="14" viewBox="0 0 24 24"><rect x="3" y="5" width="18" height="14" fill="none" stroke="#fff" stroke-width="2"/><path d="M3 6l9 7 9-7" fill="none" stroke="#fff" stroke-width="2"/></svg></span>info@FernwayAccounting.example</div>
    <div class="contact__row"><span class="contact__icon"><svg width="16" height="16" viewBox="0 0 24 24" fill="none" stroke="#fff" stroke-width="1.8"><circle cx="12" cy="12" r="9"/><ellipse cx="12" cy="12" rx="4" ry="9"/><path d="M3 12h18"/></svg></span>www.FernwayAccounting.example</div>
  </div>
</section>

<section class="card card--back" aria-label="Postcard back">
  <svg class="shapes" viewBox="0 0 930 620" preserveAspectRatio="none" aria-hidden="true">
    <defs>
      <linearGradient id="stripeB" x1="0" y1="0" x2="0" y2="1">
        <stop offset="0" stop-color="#22a9c2"/><stop offset="1" stop-color="#1c2f66"/>
      </linearGradient>
      <linearGradient id="stripeC" x1="0" y1="0" x2="0" y2="1">
        <stop offset="0" stop-color="#1c2f66"/><stop offset="1" stop-color="#22a9c2"/>
      </linearGradient>
    </defs>
    <polygon points="0,0 400,0 497,310 0,310" fill="#1c2f66"/>
    <polygon points="405,0 450,0 520,186 475,186" fill="url(#stripeC)"/>
    <polygon points="445,0 480,0 518,110 483,110" fill="#1c2f66"/>
    <polygon points="0,440 520,440 545,620 0,620" fill="#E8F1F8"/>
    <polygon points="465,330 480,330 580,620 565,620" fill="#E8F1F8"/>
    <polygon points="475,330 500,330 600,620 575,620" fill="url(#stripeB)"/>
    <polygon points="450,480 470,480 520,620 500,620" fill="url(#stripeB)"/>
  </svg>

  <div class="abs pill services-title">SERVICES</div>

  <div class="service" style="left:32px"><span class="service__icon"><svg width="26" height="26" viewBox="0 0 24 24" fill="none" stroke="#1c2f66" stroke-width="1.6"><ellipse cx="9" cy="6" rx="6" ry="2.5"/><path d="M3 6v10c0 1.4 2.7 2.5 6 2.5"/><circle cx="16" cy="15" r="5"/><path d="M16 12.5v5"/></svg></span>Bookkeeping</div>
  <div class="service" style="left:140px"><span class="service__icon"><svg width="26" height="26" viewBox="0 0 24 24" fill="none" stroke="#1c2f66" stroke-width="1.6"><rect x="5" y="3" width="14" height="18"/><path d="M8 17v-3M12 17v-6M16 17v-4M8 7h8"/></svg></span>Financial Reporting</div>
  <div class="service" style="left:292px"><span class="service__icon"><svg width="26" height="26" viewBox="0 0 24 24" fill="none" stroke="#1c2f66" stroke-width="1.6"><circle cx="7" cy="7" r="3"/><circle cx="17" cy="7" r="3"/><circle cx="7" cy="17" r="3"/><circle cx="17" cy="17" r="3"/><path d="M10 7h4M10 17h4M7 10v4M17 10v4"/></svg></span>Payroll Processing</div>

  <div class="abs packages-title">Bookkeeping Packages :</div>
  <ul class="pkg" style="left:32px"><li>Inventory</li><li>Payroll</li><li>Accruals/<br>Adjusting Entries</li></ul>
  <ul class="pkg" style="left:180px"><li>Accounts<br>Receivable</li><li>Accounts<br>Payable</li></ul>
  <ul class="pkg" style="left:290px"><li>Sales Tax</li><li>Consulting</li><li>Financial Reporting</li><li>Account Reconciliation</li></ul>

  <div class="abs badges" role="img" aria-label="Membership badges: Pine Hollow Chamber of Commerce, Continental Guild of Certified Ledgerkeepers, TallyHive certification, Federated League of Female Enterprise Founders">
    <span class="badge"></span><span class="badge-divider"></span>
    <span class="badge"></span><span class="badge-divider"></span>
    <span class="badge badge--shield"></span><span class="badge-divider"></span>
    <span class="badge badge--ring"></span>
  </div>

  <div class="abs pill" style="left:32px;top:435px">Contact Us</div>
  <div class="abs contact" style="top:492px">
    <div class="contact__row contact__row--bold"><span class="contact__icon"><svg width="14" height="14" viewBox="0 0 24 24"><path d="M6.6 10.8a15 15 0 0 0 6.6 6.6l2.2-2.2a1 1 0 0 1 1-.25 11.4 11.4 0 0 0 3.6.6 1 1 0 0 1 1 1V20a1 1 0 0 1-1 1A17 17 0 0 1 3 4a1 1 0 0 1 1-1h3.5a1 1 0 0 1 1 1c0 1.25.2 2.45.6 3.6a1 1 0 0 1-.25 1z" fill="#fff"/></svg></span>555.203.8841 / 1.800.555.0142</div>
    <div class="contact__row"><span class="contact__icon"><svg width="14" height="14" viewBox="0 0 24 24"><rect x="3" y="5" width="18" height="14" fill="none" stroke="#fff" stroke-width="2"/><path d="M3 6l9 7 9-7" fill="none" stroke="#fff" stroke-width="2"/></svg></span>info@FernwayAccounting.example</div>
    <div class="contact__row"><span class="contact__icon"><svg width="16" height="16" viewBox="0 0 24 24" fill="none" stroke="#fff" stroke-width="1.8"><circle cx="12" cy="12" r="9"/><ellipse cx="12" cy="12" rx="4" ry="9"/><path d="M3 12h18"/></svg></span>www.FernwayAccounting.example</div>
  </div>

  <div class="abs indicia">PRSRT STD<br>ECRWSS<br>U.S.POSTAGE<br>PAID<br>PLMX RETAIL</div>
  <span class="address-line" style="top:265px;left:519px"></span>
  <span class="address-line" style="top:330px;left:541px"></span>
  <span class="address-line" style="top:395px;left:562px"></span>
</section>

</body>
</html>
```